Empresa de tecnología busca diseño de tarjetas de presentación

Se requiere tarjeta de presentación impresa, con los datos de contacto y logo de la empresa. (se adjunta una imagen como referencia, esto no significa que deberá de ser igual)

```html
<!DOCTYPE html>
<html lang="es">
<head>
<meta charset="UTF-8">
<title>Aldeva Tech — Tarjetas de presentación</title>
<link rel="stylesheet" href="https://fonts.googleapis.com/css2?family=Lato:wght@400;700;900&display=swap">
<style>
  :root {
    --navy: #1b3e74;
    --green: #5dba3b;
    --ink: #222222;
    --paper: #ffffff;
    --backdrop: #e6e7ea;
  }
  * { margin: 0; padding: 0; box-sizing: border-box; }
  html, body { width: 1200px; height: 900px; overflow: hidden; }
  body {
    background: var(--backdrop);
    font-family: 'Lato', sans-serif;
    position: relative;
  }
  .card {
    position: absolute;
    width: 630px;
    height: 360px;
    border-radius: 30px;
    overflow: hidden;
  }
  .card--front {
    left: 60px; top: 60px;
    background: var(--navy);
    display: flex; align-items: center; justify-content: center;
  }
  .card--back {
    right: 60px; bottom: 60px;
    background: var(--paper);
  }
  .brand {
    font-family: 'Lato', sans-serif;
    font-weight: 700;
    letter-spacing: 0;
    white-space: nowrap;
    line-height: 1;
  }
  .card--front .brand { color: #ffffff; font-size: 56px; }
  .card--back .brand {
    position: absolute; left: 44px; top: 68px;
    color: var(--navy); font-size: 44px;
  }
  .person {
    position: absolute; right: 40px; top: 54px; text-align: right;
  }
  .person__name { font-weight: 900; font-size: 30px; line-height: 1.1; }
  .person__first { color: var(--green); }
  .person__last { color: var(--navy); }
  .person__role { font-size: 17px; color: var(--ink); margin-top: 4px; }
  .divider {
    position: absolute; left: 44px; right: 40px; top: 166px;
    height: 2px; background: var(--green);
  }
  .contact {
    position: absolute; left: 44px; top: 194px;
    list-style: none;
  }
  .contact__item {
    display: flex; align-items: center; gap: 18px;
    font-size: 19px; color: var(--ink);
    height: 42px;
  }
  .contact__icon { width: 26px; height: 26px; flex: none; }
  .address {
    position: absolute; right: 40px; top: 204px;
    font-size: 18px; color: var(--ink);
  }
</style>
</head>
<body>
  <section class="card card--front" aria-label="Frente de la tarjeta">
    <div class="brand">Aldeva Tech</div>
  </section>

  <section class="card card--back" aria-label="Reverso de la tarjeta">
    <div class="brand">Aldeva Tech</div>

    <div class="person">
      <p class="person__name"><span class="person__first">Valeria</span> <span class="person__last">Ortiz</span></p>
      <p class="person__role">Gerente Marketing Digital</p>
    </div>

    <div class="divider"></div>

    <ul class="contact">
      <li class="contact__item">
        <svg class="contact__icon" viewBox="0 0 26 26" aria-hidden="true">
          <path d="M3 10 Q13 3 23 10 L21 13 L17 11 L17 9 Q13 8 9 9 L9 11 L5 13 Z" fill="var(--green)"/>
          <rect x="5" y="14" width="16" height="9" rx="2" fill="var(--green)"/>
          <circle cx="13" cy="18.5" r="2.6" fill="#fff"/>
        </svg>
        (55)4000 2468 ext. 210
      </li>
      <li class="contact__item">
        <svg class="contact__icon" viewBox="0 0 26 26" aria-hidden="true">
          <rect x="7" y="2" width="12" height="22" rx="2.5" fill="none" stroke="var(--green)" stroke-width="2.2"/>
          <circle cx="13" cy="20" r="1.3" fill="var(--green)"/>
        </svg>
        55 2207 0419
      </li>
      <li class="contact__item">
        <svg class="contact__icon" viewBox="0 0 26 26" aria-hidden="true">
          <rect x="2" y="6" width="22" height="15" fill="var(--green)"/>
          <path d="M2 6 L13 15 L24 6 M2 21 L10 13 M24 21 L16 13" fill="none" stroke="#fff" stroke-width="1.5"/>
        </svg>
        vale.ortiz@aldevatech.com
      </li>
    </ul>

    <p class="address">Piso 12, Torre Alcor CDMX</p>
  </section>
</body>
</html>
```